Camp Brindlemoor "The '63 Circle"

We are looking for someone to design a bi-fold brochure that will help with our fundraising program. We are a Christian camp and retreat center. It would be a good idea to visit our website to get a feel for what we do, campbrindlemoor.org.

This link, https://files.examplecloud.net/share/7QxT2mKpLa9RvZc4NbHw8YeJ3sDf0UgXo?view=open, will provide you with pictures you can use and the text that will be needed. Don't expect all the pictures to be used, but wanted to provide some choices. The text that is provided will need to be used on the inside portion of the brochure.

Target Market(s)

Donors age range 25-70

Industry/Entity Type

Recreation

Requirements
Must have
• Text included in Google Drive. A few pictures. Brindlemoor Logo
Nice to have
• Professional Design
Should not have
• No clip art, no extra text (even from the website)

```html
<!DOCTYPE html>
<html lang="en">
<head>
<meta charset="utf-8">
<title>Camp Brindlemoor Brochure</title>
<link rel="stylesheet" href="https://fonts.googleapis.com/css2?family=Open+Sans:ital,wght@0,400;0,700;1,600;1,700&family=Saira+Extra+Condensed:wght@700;800&display=swap">
<style>
  :root {
    --bg: #e2e2e2;
    --olive: #7a7a3c;
    --olive-light: #a4a26a;
    --green: #2d8a66;
    --green-deep: #1f6e4f;
    --teal: #3e9e80;
    --orange: #e28a3c;
    --orange-light: #eea868;
    --white: #ffffff;
    --paper: #f2f2f0;
    --ink: #3b3b3b;
    --quote-green: #1d7050;
  }
  * { box-sizing: border-box; margin: 0; padding: 0; }
  html, body { width: 1200px; height: 2436px; overflow: hidden; background: var(--bg); }
  .canvas { position: relative; width: 1200px; height: 2436px; overflow: hidden; font-family: "Open Sans", Arial, sans-serif; }
  .page-set { position: absolute; left: 60px; height: 764px; box-shadow: 0 10px 28px rgba(0,0,0,.18); overflow: hidden; background: var(--paper); }
  .page-set svg.art { position: absolute; inset: 0; }
  .cover-solo { top: 40px; left: 330px; width: 540px; }
  .inside-spread { top: 844px; width: 1080px; }
  .outside-spread { top: 1648px; width: 1080px; }
  .spine { position: absolute; top: 0; bottom: 0; left: 540px; width: 2px; background: rgba(0,0,0,.08); }

  .cover { position: absolute; top: 0; width: 540px; height: 764px; }
  .cover-title {
    position: absolute; left: 40px; right: 38px; top: 548px; text-align: right;
    font-family: "Saira Extra Condensed", "Arial Narrow", sans-serif; font-weight: 800;
    color: var(--white); text-transform: uppercase; font-size: 42px; line-height: 1.05; letter-spacing: 0;
    white-space: nowrap;
  }
  .brand-badge {
    position: absolute; width: 124px; height: 124px; border-radius: 50%; background: var(--white);
    display: flex; align-items: center; justify-content: center; text-align: center; padding: 12px;
    font-family: "Open Sans", Arial, sans-serif; font-weight: 700;
    color: var(--green-deep); font-size: 13px; line-height: 1.2; text-transform: uppercase; letter-spacing: 0;
    box-shadow: 0 4px 10px rgba(0,0,0,.2);
  }
  .cover .brand-badge { left: 62px; top: 404px; }

  .heading {
    font-family: "Saira Extra Condensed", "Arial Narrow", sans-serif; font-weight: 800;
    text-transform: uppercase; color: var(--white); letter-spacing: 0; line-height: 1;
  }
  .about-heading { position: absolute; left: 50px; top: 34px; font-size: 44px; white-space: nowrap; }
  .about-intro { position: absolute; left: 50px; top: 92px; width: 450px; color: var(--white); font-size: 13px; line-height: 1.45; }
  .values-text { position: absolute; left: 610px; top: 70px; width: 420px; color: var(--white); font-size: 14px; line-height: 1.5; text-align: justify; }
  .cost-quote { position: absolute; left: 50px; top: 400px; width: 380px; color: var(--quote-green); font-style: italic; font-weight: 700; font-size: 22px; line-height: 1.2; }
  .club-text { position: absolute; left: 50px; top: 590px; width: 440px; color: var(--ink); font-size: 13px; line-height: 1.5; }
  .support-lead { position: absolute; left: 590px; top: 592px; width: 440px; color: var(--ink); font-size: 13px; line-height: 1.4; font-weight: 700; }
  .support-text { position: absolute; left: 590px; top: 650px; width: 440px; color: var(--ink); font-size: 12.5px; line-height: 1.4; text-align: justify; }

  .back-page { position: absolute; left: 0; top: 0; width: 540px; height: 764px; text-align: center; color: var(--white); }
  .mission-heading { position: absolute; left: 0; right: 0; top: 150px; font-size: 36px; }
  .mission-text { position: absolute; left: 70px; right: 70px; top: 200px; font-size: 13px; line-height: 1.5; }
  .contact-heading { position: absolute; left: 0; right: 0; top: 320px; font-size: 36px; }
  .contact-list { position: absolute; left: 0; right: 0; top: 372px; list-style: none; font-size: 14px; font-weight: 700; line-height: 1.9; }
  .back-page .brand-badge { left: 208px; top: 520px; }
  .outside-spread .cover { left: 540px; }
</style>
</head>
<body>
<main class="canvas">

  <section class="page-set cover-solo" aria-label="Front cover">
    <div class="cover" style="left:0">
      <svg class="art" width="540" height="764" viewBox="0 0 540 764">
        <defs>
          <linearGradient id="coverBgA" x1="0" y1="0" x2="0.6" y2="1">
            <stop offset="0" stop-color="#7d7b3d"/><stop offset="0.55" stop-color="#3f8050"/><stop offset="1" stop-color="#3a9a7c"/>
          </linearGradient>
          <radialGradient id="photoA" cx="0.5" cy="0.45" r="0.7">
            <stop offset="0" stop-color="#6a4a6a"/><stop offset="0.35" stop-color="#3c4b8c"/><stop offset="0.7" stop-color="#3f6b34"/><stop offset="1" stop-color="#22401f"/>
          </radialGradient>
        </defs>
        <rect width="540" height="764" fill="url(#coverBgA)"/>
        <circle cx="360" cy="230" r="320" fill="var(--orange)"/>
        <circle cx="372" cy="214" r="306" fill="url(#photoA)" role="img" aria-label="Photo of smiling campers in life jackets by the water"/>
      </svg>
      <div class="brand-badge">Camp Brindlemoor</div>
      <h1 class="cover-title">Christian Camp<br>And Retreat<br>Center Facility</h1>
    </div>
  </section>

  <section class="page-set inside-spread" aria-label="Inside spread">
    <svg class="art" width="1080" height="764" viewBox="0 0 1080 764">
      <defs>
        <linearGradient id="bandGrad" x1="0" y1="0" x2="1" y2="0.3">
          <stop offset="0" stop-color="#e0883a"/><stop offset="0.38" stop-color="#a6a06a"/><stop offset="0.55" stop-color="#5e8052"/><stop offset="1" stop-color="#2c8a69"/>
        </linearGradient>
        <linearGradient id="ringGrad" x1="0" y1="0" x2="1" y2="1">
          <stop offset="0" stop-color="#e28a3c"/><stop offset="1" stop-color="#8a8a4a"/>
        </linearGradient>
        <linearGradient id="shotGrad" x1="0" y1="0" x2="0" y2="1">
          <stop offset="0" stop-color="#8fae7a"/><stop offset="1" stop-color="#5a6e45"/>
        </linearGradient>
      </defs>
      <path d="M0 0 H1080 V560 Q 880 600 720 420 Q 540 220 0 210 Z" fill="var(--orange)"/>
      <path d="M0 0 H1080 V540 Q 880 580 720 400 Q 540 200 0 190 Z" fill="url(#bandGrad)"/>
      <g fill="url(#shotGrad)" stroke="url(#ringGrad)" stroke-width="8">
        <circle cx="140" cy="270" r="66" role="img" aria-label="Photo of the camp entrance sign among trees"/>
        <circle cx="320" cy="310" r="66" role="img" aria-label="Photo of campers covered in shaving cream"/>
        <circle cx="510" cy="370" r="66" role="img" aria-label="Photo of the camp dining hall"/>
        <circle cx="700" cy="440" r="66" role="img" aria-label="Photo of campers giving a high five"/>
        <circle cx="890" cy="510" r="66" role="img" aria-label="Photo of a cabin group"/>
      </g>
    </svg>
    <div class="spine"></div>
    <h2 class="heading about-heading">About Brindlemoor</h2>
    <p class="about-intro">Camp Brindlemoor was established in 1948 by Harold &amp; Edith Lantry and many other families to provide a place where children would have the opportunity to Encounter Christ, Community &amp; Creation. The founders of Brindlemoor wanted to provide a great experience at a reasonable price.</p>
    <p class="values-text">We are committed to continuing that same core value. We don't believe that an incredible camp experience should only be for kids who can afford an incredible camp experience. We believe strongly that Christian Camping is a great mission field where lives are changed forever.</p>
    <p class="cost-quote">It cost Brindlemoor just over $500 for a one-week camper and around $800 for a two-week camper. We currently charge $285 for a one-week session and $425</p>
    <p class="club-text">In an effort to keep camper fees at a reasonable level we established The '63 Circle. Members of The '63 Circle are former campers, counselors and families that have been impacted by the ministry of Brindlemoor. They believe in the mission of Christian camping.</p>
    <p class="support-lead">By providing monthly support they help to defray some of the cost for campers, which allows more children to attend Brindlemoor each summer and facility updates</p>
    <p class="support-text">We hope you will consider joining this effort. Recurring donations can be set up at campbrindlemoor.org by clicking on the "Give Now" button at the top of the page and selecting the subaccount "The '63 Circle." Be sure to choose your recurring date before clicking the "submit" button. Checks can be mailed to P.O. Box 4410, Alder Springs, AR 72199.</p>
  </section>

  <section class="page-set outside-spread" aria-label="Back and front cover">
    <svg class="art" width="1080" height="764" viewBox="0 0 1080 764">
      <defs>
        <linearGradient id="backGrad" x1="0" y1="0.2" x2="1" y2="0.8">
          <stop offset="0" stop-color="#e38a3c"/><stop offset="0.45" stop-color="#b18a4a"/><stop offset="0.75" stop-color="#4f7e50"/><stop offset="1" stop-color="#2c8a69"/>
        </linearGradient>
        <linearGradient id="coverBgB" x1="0" y1="0" x2="0.6" y2="1">
          <stop offset="0" stop-color="#7d7b3d"/><stop offset="0.55" stop-color="#3f8050"/><stop offset="1" stop-color="#3a9a7c"/>
        </linearGradient>
        <radialGradient id="photoB" cx="0.5" cy="0.45" r="0.7">
          <stop offset="0" stop-color="#6a4a6a"/><stop offset="0.35" stop-color="#3c4b8c"/><stop offset="0.7" stop-color="#3f6b34"/><stop offset="1" stop-color="#22401f"/>
        </radialGradient>
        <clipPath id="frontClip"><rect x="540" y="0" width="540" height="764"/></clipPath>
      </defs>
      <rect x="0" y="0" width="540" height="764" fill="url(#backGrad)" role="img" aria-label="Faint background photo of a campfire gathering"/>
      <g clip-path="url(#frontClip)">
        <rect x="540" width="540" height="764" fill="url(#coverBgB)"/>
        <circle cx="900" cy="230" r="320" fill="var(--orange)"/>
        <circle cx="912" cy="214" r="306" fill="url(#photoB)" role="img" aria-label="Photo of smiling campers in life jackets by the water"/>
      </g>
    </svg>
    <div class="spine"></div>
    <div class="back-page">
      <h2 class="heading mission-heading">Our Mission</h2>
      <p class="mission-text">We want to strengthen young people's relationship with Christ through meaningful worship experiences, create an environment that promotes community through Christ-centered relationships, and provide opportunities to experience God's presence through His creation.</p>
      <h2 class="heading contact-heading">Contact Us</h2>
      <ul class="contact-list">
        <li>555-214-0187</li>
        <li>office@campbrindlemoor.org</li>
        <li>48 Hollow Creek Road Alder Springs, AR 72199</li>
        <li>www.campbrindlemoor.org</li>
      </ul>
      <div class="brand-badge">Camp Brindlemoor</div>
    </div>
    <div class="cover">
      <div class="brand-badge">Camp Brindlemoor</div>
      <h2 class="cover-title">Christian Camp<br>And Retreat<br>Center Facility</h2>
    </div>
  </section>

</main>
</body>
</html>
```